DEAN COLLOPY PROPERTY SERVICES

I want a business card that is clean and simple.
'Dean Collopy Property Services' is the title.
Somewhere on the card needs to be 'Carpentry, Tiling, painting and garden services'

On the back of card
PH 087 394 1526
email: deancollopypropertyservices@fernmail.net

I have attached a picture of my other business. I would like the font and design to be similar to the bathroom business.

Many thanks.

```html
<!DOCTYPE html>
<html lang="en">
<head>
<meta charset="utf-8">
<title>Dean Collopy Property Services – Business Card</title>
<link rel="stylesheet" href="https://fonts.googleapis.com/css2?family=Montserrat:wght@400;600&family=Open+Sans:wght@400;600&display=swap">
<style>
  :root {
    --backdrop: #e9e9ea;
    --ink: #0b0b0b;
    --paper: #ffffff;
    --muted: #3a3a3a;
    --card-shadow: 0 14px 30px rgba(0, 0, 0, 0.18);
  }
  * { box-sizing: border-box; margin: 0; padding: 0; }
  html, body {
    width: 1200px;
    height: 800px;
    overflow: hidden;
    background: var(--backdrop);
  }
  .canvas {
    position: relative;
    width: 1200px;
    height: 800px;
    display: flex;
    align-items: center;
    justify-content: center;
    gap: 60px;
  }
  .card {
    position: relative;
    width: 520px;
    height: 297px;
    box-shadow: var(--card-shadow);
  }
  .card--front { background: var(--ink); color: var(--paper); }
  .card--back { background: var(--paper); color: var(--ink); }

  .wordmark {
    font-family: "Montserrat", sans-serif;
    display: inline-flex;
    flex-direction: column;
    align-items: flex-end;
    line-height: 1;
  }
  .wordmark__name { font-weight: 600; letter-spacing: 0.5px; }
  .wordmark__tagline {
    font-weight: 400;
    text-transform: uppercase;
    letter-spacing: 1.6px;
    margin-top: 4px;
  }

  .card--front .wordmark {
    position: absolute;
    left: 50%;
    top: 104px;
    transform: translateX(-50%);
  }
  .card--front .wordmark__name { font-size: 42px; }
  .card--front .wordmark__tagline { font-size: 11px; }

  .service-list {
    position: absolute;
    left: 0;
    right: 0;
    bottom: 40px;
    display: flex;
    justify-content: center;
    gap: 14px;
    list-style: none;
    font-family: "Montserrat", sans-serif;
    font-size: 12.5px;
    letter-spacing: 0.3px;
  }
  .service-list li::before {
    content: "";
    display: inline-block;
    width: 5px;
    height: 5px;
    border-radius: 50%;
    background: var(--paper);
    margin-right: 5px;
    vertical-align: middle;
  }

  .card--back .wordmark {
    position: absolute;
    right: 36px;
    top: 42px;
  }
  .card--back .wordmark__name { font-size: 27px; }
  .card--back .wordmark__tagline { font-size: 8px; letter-spacing: 1.3px; margin-top: 3px; }

  .contact {
    position: absolute;
    left: 40px;
    bottom: 40px;
    font-family: "Open Sans", sans-serif;
    font-size: 13px;
    color: var(--muted);
  }
  .contact__name { font-weight: 600; font-size: 14.5px; color: var(--ink); }
  .contact__role { margin-bottom: 10px; }
  .contact__line { display: flex; align-items: center; gap: 7px; line-height: 1.5; }
  .contact__icon { width: 11px; height: 11px; fill: var(--ink); flex: none; }
</style>
</head>
<body>
<main class="canvas">
  <section class="card card--front" aria-label="Card front">
    <div class="wordmark">
      <span class="wordmark__name">Dean Collopy</span>
      <span class="wordmark__tagline">Property Services</span>
    </div>
    <ul class="service-list">
      <li>Carpentry</li>
      <li>Tiling</li>
      <li>Painting and garden services</li>
    </ul>
  </section>

  <section class="card card--back" aria-label="Card back">
    <div class="wordmark">
      <span class="wordmark__name">Dean Collopy</span>
      <span class="wordmark__tagline">Property Services</span>
    </div>
    <div class="contact">
      <p class="contact__name">Dean Collopy</p>
      <p class="contact__role">President</p>
      <p class="contact__line">
        <svg class="contact__icon" viewBox="0 0 24 24" aria-hidden="true"><path d="M6.6 10.8a15.2 15.2 0 0 0 6.6 6.6l2.2-2.2a1 1 0 0 1 1-.25 11.4 11.4 0 0 0 3.6.57 1 1 0 0 1 1 1V20a1 1 0 0 1-1 1A17 17 0 0 1 3 4a1 1 0 0 1 1-1h3.5a1 1 0 0 1 1 1c0 1.25.2 2.46.57 3.6a1 1 0 0 1-.25 1z"/></svg>
        <span>087 394 1526</span>
      </p>
      <p class="contact__line">
        <svg class="contact__icon" viewBox="0 0 24 24" aria-hidden="true"><path d="M2 5h20v14H2z M3.5 6.5v.4l8.5 6 8.5-6v-.4z" fill-rule="evenodd"/></svg>
        <span>deancollopypropertyservices@fernmail.net</span>
      </p>
    </div>
  </section>
</main>
</body>
</html>
```